KESTIVA GROUP OF CLINICS

We need a medical & lab report file. The design should be healthcare related. Our current file design has been used for almost 10 years. We need something more fresh & up-to-date. We have attached the current file design.

```html
<!DOCTYPE html>
<html lang="en">
<head>
<meta charset="utf-8">
<title>Kestiva Group of Clinics – Medical Report File</title>
<link href="https://fonts.googleapis.com/css2?family=Montserrat:wght@400;500;600;700;800&display=swap" rel="stylesheet">
<style>
:root{
  --backdrop:#c2c3c6;
  --paper:#ffffff;
  --sky:#92d6f6;
  --royal:#2b5cb2;
  --cyan:#0a9ce0;
  --brand-blue:#1f9fe8;
  --brand-indigo:#3b3d98;
  --ink:#1d1d1f;
  --muted:#55575c;
  --alert:#e4161d;
}
*{margin:0;padding:0;box-sizing:border-box}
html,body{width:1200px;height:849px;overflow:hidden}
body{background:var(--backdrop);font-family:"Montserrat",sans-serif;color:var(--ink);position:relative}
.spread{position:absolute;left:108px;top:77px;width:984px;height:695px;background:var(--paper);overflow:hidden}
.shapes{position:absolute;inset:0;width:984px;height:695px}
.photo-fade{position:absolute;left:150px;top:0;width:330px;height:400px;
  background:radial-gradient(ellipse at 70% 35%,rgba(160,200,225,.55),rgba(230,190,195,.35) 45%,rgba(255,255,255,0) 72%)}
.brand-dot{display:block;border-radius:50%}
.left-brand{position:absolute;left:79px;top:106px;display:flex;align-items:center;gap:10px;color:var(--brand-blue);font-weight:800}
.left-brand .brand-dot{width:48px;height:48px;background:var(--brand-blue);flex:none}
.left-brand .name{line-height:1}
.left-brand .name-main{display:block;font-size:44px;letter-spacing:-1px}
.left-brand .name-sub{display:block;font-size:17px;letter-spacing:-.3px;margin-top:2px}
.clinic-list{position:absolute;left:79px;top:179px;display:flex;flex-direction:column;gap:6.5px}
.clinic h3{font-size:11.4px;font-weight:700;letter-spacing:-.4px;line-height:12px}
.clinic p{font-size:9.3px;font-weight:400;letter-spacing:-.25px;line-height:10.9px}
.clinic b{font-weight:700}
.clinic .mail{margin-left:12px}
.right-brand{position:absolute;left:492px;top:72px;width:272px;text-align:center}
.right-brand .brand-dot{width:40px;height:40px;margin:0 auto 48px;background:var(--brand-indigo)}
.right-brand .name{font-size:18px;font-weight:700;color:var(--brand-indigo);letter-spacing:-.4px;line-height:1}
.tagline{font-size:10px;font-weight:500;color:var(--muted);margin-top:6px;letter-spacing:.2px}
.title{position:absolute;left:549px;top:440px;line-height:1}
.title .t1{display:block;font-size:44px;font-weight:400;letter-spacing:-.5px}
.title .t2{display:block;font-size:51px;font-weight:800;letter-spacing:-1px;margin-top:-3px}
.fields{position:absolute;left:550px;top:558px;width:368px;display:flex;flex-direction:column;gap:7px}
.field{display:flex;align-items:flex-end;font-size:12px;font-weight:500;height:15px}
.field .line{flex:1;border-bottom:2px dashed var(--ink);margin-left:2px;margin-bottom:2px}
.confidential{position:absolute;left:549px;top:643px;font-size:12.5px;font-weight:700;color:var(--alert);letter-spacing:-.3px}
</style>
</head>
<body>
<main class="spread">
  <div class="photo-fade" role="img" aria-label="Faded photo of a doctor with stethoscope and a translucent heart"></div>
  <svg class="shapes" viewBox="0 0 984 695">
    <defs>
      <linearGradient id="deepBlue" x1="0" y1="0" x2="0" y2="1">
        <stop offset="0" stop-color="#2b5cb2"/><stop offset="1" stop-color="#0a9ce0"/>
      </linearGradient>
      <linearGradient id="coverPhoto" x1="0" y1="0" x2="1" y2="1">
        <stop offset="0" stop-color="#bfe2f7"/><stop offset="1" stop-color="#5fb4e6"/>
      </linearGradient>
      <linearGradient id="teamPhoto" x1="0" y1="0" x2="1" y2="0">
        <stop offset="0" stop-color="#a9d6f0"/><stop offset=".55" stop-color="#e7f3fb"/><stop offset="1" stop-color="#cde9f8"/>
      </linearGradient>
    </defs>
    <polygon points="386,0 492,0 492,695 420,695" fill="var(--sky)"/>
    <polygon points="357,517 467,480 467,695 357,695" fill="url(#deepBlue)"/>
    <polygon points="755,0 984,0 984,392 908,386" fill="url(#coverPhoto)" role="img" aria-label="Photo of a doctor holding a glowing anatomical heart"/>
    <polygon points="492,211 867,211 911,386 492,386" fill="url(#teamPhoto)" role="img" aria-label="Photo of two doctors in discussion with medical hexagon graphics"/>
    <polygon points="787,404 853,404 893,514 830,514" fill="var(--sky)"/>
    <polygon points="858,404 984,404 984,514 898,514" fill="url(#deepBlue)"/>
    <polygon points="492,678 954,678 963,695 492,695" fill="var(--sky)"/>
    <polygon points="955,678 984,678 984,695 963,695" fill="var(--royal)"/>
  </svg>

  <div class="left-brand">
    <span class="brand-dot"></span>
    <span class="name"><span class="name-main">KESTIVA</span><span class="name-sub">GROUP OF CLINICS</span></span>
  </div>

  <section class="clinic-list">
    <article class="clinic"><h3>PUSAT PERUBATAN KESTIVA</h3>
      <p>Level 12, Orkid Tower, No. 8, Jalan Cempaka Raya,</p>
      <p>Off Jalan Seri Cempaka, 50480 Kuala Lumpur,</p>
      <p>Tel No: <b>+603-2100 4810</b></p>
      <p>Fax No: <b>+603-2100 4811</b><span class="mail">Email: care@kestiva-clinic.my</span></p></article>
    <article class="clinic"><h3>KLINIK KESTIVA (TAMAN SERI MELUR)</h3>
      <p>No. 22, Jalan Melur 4/B, Taman Seri Melur,</p>
      <p>40460 Shah Alam, Selangor Darul Ehsan.</p>
      <p>Tel No: <b>+603-5120 3301</b></p>
      <p>Fax No: <b>+603-5120 3302</b><span class="mail">Email: care@kestiva-clinic.my</span></p></article>
    <article class="clinic"><h3>KLINIK KESTIVA (BATU KEMUNING)</h3>
      <p>Lot 2A-1-1, 2A-1-2, 2A-1-3,</p>
      <p>Persiaran Kemuning, Kemuning Square, 11920 Batu Kemuning, Penang.</p>
      <p>Tel No: <b>+604-310 2240</b></p>
      <p>Fax No: <b>+604-310 2241</b><span class="mail">Email: kemuning@kestiva-clinic.my</span></p></article>
    <article class="clinic"><h3>KLINIK KESTIVA (BANDAR DAHLIA)</h3>
      <p>No. 54, Jalan Niaga Dahlia 2/5, Pusat Niaga Bandar Dahlia,</p>
      <p>71960 Bandar Dahlia, Negeri Sembilan.</p>
      <p>Tel No: <b>+606-455 1800</b></p>
      <p>Fax No: <b>+606-455 1807</b><span class="mail">Email: dahlia@kestiva-clinic.my</span></p></article>
    <article class="clinic"><h3>KESTIVA MEDICAL CLINIC (TERMINAL A)</h3>
      <p>Lot TA 12, Arrival Hall, Main Terminal Building,</p>
      <p>Terminal A, 64010 Sepang, Selangor Darul Ehsan.</p>
      <p>Tel No: <b>+603-8610 2200</b></p>
      <p>Fax No: <b>+603-8610 2201</b><span class="mail">Email: terminala@kestiva-clinic.my</span></p></article>
    <article class="clinic"><h3>KESTIVA MEDICAL CLINIC (TERMINAL B)</h3>
      <p>B2-1-07, Landside Arrival Hall,</p>
      <p>Terminal B, 64020 Sepang, Selangor Darul Ehsan.</p>
      <p>Tel No: <b>+603-8620 3300</b></p>
      <p>Fax No: <b>+603-8620 3301</b><span class="mail">Email: terminalb@kestiva-clinic.my</span></p></article>
    <article class="clinic"><h3>KESTIVA MEDICAL CLINIC (NORTH PORT)</h3>
      <p>Unit 1-05 Level 1, Passenger Hall Building,</p>
      <p>North Port Air Terminal, 11930 Batu Kemuning, Penang.</p>
      <p>Tel No: <b>+604-520 6600</b></p>
      <p>Fax No: <b>+604-520 6601</b><span class="mail">Email: northport@kestiva-clinic.my</span></p></article>
  </section>

  <div class="right-brand">
    <span class="brand-dot"></span>
    <div class="name">KESTIVA GROUP</div>
    <div class="tagline">caring for every family</div>
  </div>

  <h1 class="title"><span class="t1">MEDICAL</span><span class="t2">REPORT</span></h1>

  <div class="fields">
    <div class="field">NAME<span class="line"></span></div>
    <div class="field">ADDRESS<span class="line"></span></div>
    <div class="field">DATE<span class="line"></span></div>
  </div>

  <p class="confidential">PRIVATE AND CONFIDENTIAL</p>
</main>
</body>
</html>
```